Corsets, Cups and Commerce needs a book cover

I've been in lingerie business for 12 years, we own 5 x Lingerie stores. This is my story aimed at women in business or women who want to start a business. Essentially its a business book but also offers bra fitting advice. Although the book cover can be a bit cheeky it also needs to be tasteful. I do not have a colour in mind I just don't like it too girly. I like strong and bold with a feminine touch. The title needs to catch peoples attention when surrounded by so many other books. It needs to have some sort of image or texture. That could be a lace background texture. I like the idea of a bra hanging off the letters or some kind of image of a bra but a beautiful lacy bra. I would like the cover to be more beautiful than tacky even though it has the word 'boobs'.
Updates

Hi everyone, some great designs so far. Many of you have made a bra part of the 'Boobs' word. I thought this could work but it doesn't as it covers up the word 'Boobs' too much and I feel this word will catch peoples attention. If any of you would like to revise please feel free. thankyou Delphine.

Target Market(s)

Women in business or women wanting to start a business.

Industry/Entity Type

Retail

Logo Text

Corsets, Cups and Commerce

Font styles to use
Serif
Sans Serif

Colors

Designer to choose colors to be used in the design.

Requirements
Must have
• Title: Corsets, Cups and Commerce (you could replace 'and' with '&' if it works better.
• Tagline: Steady Lessons for Women in Trade
• Author: Delphine Karsby
Nice to have
• An image of a bra, maybe in a playful way. It could hang off the letters or maybe the letters could look like a bra, but I'm concerned it may look tacky that way. Somehow incorporate a picture of a bra preferably as part of the title.
• I don't have images for you, you have the freedom to choose.
Should not have
• Although this book has boobs and bras in the title it must not be tacky or sexual. It is a business book.
• I do not like it to look too girly, probably not script unless its subtle.

```html
<!DOCTYPE html>
<html lang="en">
<head>
<meta charset="utf-8">
<title>Corsets, Cups and Commerce — Book Cover</title>
<link rel="stylesheet" href="https://fonts.googleapis.com/css2?family=Cabin:wght@400;500&family=Parisienne&display=swap">
<style>
  :root {
    --cover-black: #000000;
    --lace-red: #c4002f;
    --lace-red-deep: #a80028;
    --lace-red-soft: rgba(196, 0, 47, 0.55);
    --title-red: #c8002d;
    --ink-white: #ffffff;
  }
  html, body {
    margin: 0;
    padding: 0;
    width: 777px;
    height: 1200px;
    overflow: hidden;
    background: var(--cover-black);
  }
  .book-cover {
    position: relative;
    width: 777px;
    height: 1200px;
    background: var(--cover-black);
    overflow: hidden;
    font-family: "Cabin", "Gill Sans", sans-serif;
  }
  .lace-trim {
    position: absolute;
    left: 0;
    width: 777px;
  }
  .lace-trim--top {
    top: 0;
    height: 124px;
    background:
      radial-gradient(ellipse 60% 70% at 50% 0%, var(--lace-red) 0%, transparent 100%),
      linear-gradient(to bottom, var(--lace-red-deep) 0%, var(--lace-red) 25%, var(--lace-red) 70%, var(--lace-red-soft) 88%, transparent 100%);
  }
  .lace-trim--bottom {
    top: 912px;
    height: 156px;
    background:
      linear-gradient(to bottom, transparent 0%, var(--lace-red-soft) 12%, var(--lace-red) 28%, var(--lace-red) 82%, var(--lace-red-deep) 100%);
  }
  .title-block {
    position: absolute;
    left: 0;
    top: 0;
    width: 777px;
    height: 700px;
  }
  .title-word {
    fill: var(--title-red);
    font-family: "Cabin", "Gill Sans", sans-serif;
    font-weight: 400;
  }
  .title-amp {
    fill: var(--ink-white);
    font-family: "Parisienne", cursive;
  }
  .tagline {
    position: absolute;
    left: 0;
    top: 744px;
    width: 777px;
    margin: 0;
    text-align: center;
    color: var(--ink-white);
    font-size: 42px;
    line-height: 58px;
    font-weight: 400;
    letter-spacing: 2px;
    text-transform: uppercase;
  }
  .author {
    position: absolute;
    left: 0;
    top: 1104px;
    width: 777px;
    margin: 0;
    text-align: center;
    color: var(--ink-white);
    font-size: 33px;
    font-weight: 400;
    letter-spacing: 11px;
    text-transform: uppercase;
  }
</style>
</head>
<body>
  <main class="book-cover">
    <div class="lace-trim lace-trim--top" role="img" aria-label="Red scalloped lace trim with a lattice edge along the top"></div>

    <svg class="title-block" viewBox="0 0 777 700" width="777" height="700" role="img" aria-label="Corsets, Cups &amp; Commerce">
      <text class="title-word" x="148" y="268" font-size="122" textLength="476" lengthAdjust="spacingAndGlyphs">CORSETS</text>
      <text class="title-word" x="150" y="404" font-size="122" textLength="476" lengthAdjust="spacing">CUPS</text>
      <text class="title-amp" x="392" y="526" font-size="120" text-anchor="middle">&amp;</text>
      <text class="title-word" x="148" y="656" font-size="122" textLength="480" lengthAdjust="spacingAndGlyphs">COMMERCE</text>
    </svg>

    <p class="tagline">Steady Lessons<br>for Women in Trade</p>

    <div class="lace-trim lace-trim--bottom" role="img" aria-label="Red scalloped lace trim with a lattice edge above the author name"></div>

    <p class="author">Delphine Karsby</p>
  </main>
</body>
</html>
```